Industrial Company needing new business cards

We are a newly branded Industrial trade company. We specialise in Electrical, Mechanical and Air-conditioning.

I would like to see designs single sided. Focusing on the color scheme white/red/black and possibly gray. Possibly make it a black card with white writting... but open to all designs.

I would like the design to be professional, sleek and to the point.

Industry/Entity Type

Business

Contact Information for Business Card

Tom Harwick
Managing Director / Electrician
tomwork@velnet.com.au
47 Garnet Road, Rutherford NSW 2320
Mobile: 0427115830
www.harwickindustrialgroup.com.au

Requirements
Must have
• Must be able to be sent in a manner that i can change the details for each employee.
• Our logo
Nice to have
• Would like it to somehow have " incorporating Talvo Group Pty Ltd" as this is the company we have taken over.
Should not have
• No yellow!!!
• must not simply place "talvo group" randomly on the business card. refer nice to have.

```html
<!DOCTYPE html>
<html lang="en">
<head>
<meta charset="utf-8">
<title>Harwick Industrial Group – Business Card</title>
<link rel="stylesheet" href="https://fonts.googleapis.com/css2?family=Lato:wght@400;700;900&display=swap">
<style>
  :root {
    --backdrop: #e6e6e6;
    --card: #ffffff;
    --ink: #111111;
    --band: #000000;
    --red: #e31e24;
    --grey: #6d6d6d;
    --on-band: #ffffff;
  }
  * { box-sizing: border-box; margin: 0; padding: 0; }
  html, body {
    width: 1200px;
    height: 1000px;
    overflow: hidden;
    background: var(--backdrop);
    font-family: "Lato", Arial, sans-serif;
  }
  .business-card {
    position: absolute;
    left: 67px;
    top: 181px;
    width: 1066px;
    height: 637px;
    background: var(--card);
    box-shadow: 0 6px 18px rgba(0,0,0,0.18);
    overflow: hidden;
  }
  .brand {
    position: absolute;
    left: 64px;
    top: 78px;
  }
  .brand-row {
    display: flex;
    align-items: center;
    gap: 18px;
  }
  .brand-mark {
    width: 52px;
    height: 52px;
    background: var(--red);
  }
  .brand-name {
    font-weight: 900;
    font-size: 44px;
    letter-spacing: 0.5px;
    color: var(--ink);
    text-transform: uppercase;
    line-height: 1;
  }
  .brand-services {
    margin-top: 16px;
    margin-left: 70px;
    font-size: 15px;
    font-weight: 700;
    letter-spacing: 0.6px;
    color: var(--grey);
    text-transform: uppercase;
  }
  .person {
    position: absolute;
    left: 64px;
    top: 278px;
  }
  .person-name {
    font-weight: 700;
    font-size: 35px;
    color: var(--ink);
    line-height: 1.2;
  }
  .person-role {
    font-size: 27px;
    color: var(--red);
    line-height: 1.3;
  }
  .contact-band {
    position: absolute;
    left: 0;
    top: 378px;
    width: 864px;
    height: 206px;
    background: var(--band);
    clip-path: polygon(0 0, 768px 0, 864px 206px, 0 206px);
  }
  .contact-list {
    position: absolute;
    left: 62px;
    top: 394px;
    list-style: none;
    color: var(--on-band);
    font-size: 25px;
    line-height: 35px;
  }
  .contact-list li {
    display: flex;
    align-items: center;
    gap: 12px;
  }
  .contact-icon {
    width: 20px;
    height: 20px;
    flex: none;
    fill: var(--on-band);
  }
  .company-block {
    position: absolute;
    left: 62px;
    top: 500px;
    color: var(--on-band);
    font-size: 25px;
    line-height: 37px;
  }
  .company-name { font-weight: 700; }
</style>
</head>
<body>
  <article class="business-card">
    <header class="brand">
      <div class="brand-row">
        <span class="brand-mark"></span>
        <span class="brand-name">Harwick Industrial Group</span>
      </div>
      <p class="brand-services">Electrical - Mechanical - Airconditioning</p>
    </header>

    <section class="person">
      <h1 class="person-name">Tom Harwick</h1>
      <p class="person-role">Managing Director / Electrician</p>
    </section>

    <div class="contact-band"></div>

    <ul class="contact-list">
      <li>
        <svg class="contact-icon" viewBox="0 0 24 24" aria-hidden="true"><path d="M6.6 10.8a15.1 15.1 0 0 0 6.6 6.6l2.2-2.2c.3-.3.7-.4 1-.2 1.1.4 2.3.6 3.6.6.6 0 1 .4 1 1V20c0 .6-.4 1-1 1A17 17 0 0 1 3 4c0-.6.4-1 1-1h3.5c.6 0 1 .4 1 1 0 1.3.2 2.5.6 3.6.1.3 0 .7-.2 1z"/></svg>
        <span>0427115830</span>
      </li>
      <li>
        <svg class="contact-icon" viewBox="0 0 24 24" aria-hidden="true"><path d="M2 5h20v14H2z"/><path d="M2 5l10 8 10-8" fill="none" stroke="#000" stroke-width="1.6"/></svg>
        <span>tomwork@velnet.com.au</span>
      </li>
      <li>
        <svg class="contact-icon" viewBox="0 0 24 24" aria-hidden="true"><circle cx="12" cy="12" r="9" fill="none" stroke="#fff" stroke-width="2.2"/><path d="M3 12h18M12 3c3 3 3 15 0 18M12 3c-3 3-3 15 0 18" fill="none" stroke="#fff" stroke-width="1.6"/></svg>
        <span>www.harwickindustrialgroup.com.au</span>
      </li>
    </ul>

    <div class="company-block">
      <p class="company-name">Talvo Group Pty Ltd</p>
      <p class="company-address">47 Garnet Road, Elmsvale Central</p>
    </div>
  </article>
</body>
</html>
```